Seed Oil Safety Card for Healthy Restaurant Dining

I am seeking a design for a physical card to communicate my wife's health-related dietary restriction regarding seed oils. This card will be given to restaurant waiters to ensure her meals are prepared without seed oils, as it is a health issue and not merely a preference.
My wife cannot eat any “seed oil” or “processed oil”, including:
- Vegetable oil
- Canola oil
- Soybean oil
- Sunflower oil
- Corn oil
- Cottonseed oil
- Safflower oil
- Peanut oil
- Sesame oil
Oils that are OK for her to consume:
- Butter (most preferable)
- Extra virgin olive oil
- Avocado oil
- Coconut oil
- Ghee
- Lard
- Any other animal-based fats
Key Design Requirements:
- Clarity and speed of communication: The card should be easily read and understood by waiters, even in low-light environments, emphasizing that it's a health concern.
- Avoid common misconceptions: Ensure the design doesn't imply common dietary preferences like "vegetarian" or "no butter." Animal fats and butter are actually preferable for her!
- Preferred term: Use "seed oils" as the term to describe what she cannot eat due to her health issue.
- Trace amounts are acceptable: Communicate that it's OK to use cookware that has previously been in contact with seed oils, but not to have seed oil as an ingredient. Please suggest a concise way to convey this.
- Card dimensions: Design should be 3.5” x 2.25” (standard credit-card size on cardlomex.example). Horizontal or vertical layouts are both fine, whichever makes the message clearer.
Design Suggestions:
- Utilize bold and easy-to-read typography to communicate the main message.
- Consider incorporating relevant icons or graphics that help convey the message without adding confusion.
- Use contrasting colors to enhance readability, especially in low-light situations.
- To communicate the “trace amounts OK” part, consider phrases such as:
- "Cross-contamination acceptable"
- “Used cookware OK, no ingredient use”
- “Separate cookware not necessary”
Thank you for your assistance in creating this essential card for my wife's health and safety when dining out!

```html
<!DOCTYPE html>
<html lang="en">
<head>
<meta charset="utf-8">
<title>Seed Oil Safety Card – Front and Back</title>
<link rel="stylesheet" href="https://fonts.googleapis.com/css2?family=Fraunces:opsz,wght@9..144,800;9..144,900&family=Lexend:wght@400;500&family=Open+Sans:wght@400&display=swap">
<style>
  :root {
    --ink: #0a0b0a;
    --paper: #ffffff;
    --highlight: #f4eff3;
    --hand-light: #e6e6e6;
    --hand-dark: #2a2a2a;
  }
  * { margin: 0; padding: 0; box-sizing: border-box; }
  html, body { width: 1200px; height: 1133px; overflow: hidden; background: var(--paper); }
  .sheet { position: relative; width: 1200px; height: 1133px; font-family: "Lexend", sans-serif; color: var(--ink); }

  .side-label {
    position: absolute; left: 4px;
    font-family: "Open Sans", sans-serif; font-size: 84px; font-weight: 400; line-height: 1;
  }
  .side-label--front { top: 236px; }
  .side-label--back { top: 825px; left: 14px; }

  .dimension { position: absolute; left: 0; top: 0; overflow: visible; }
  .dimension-text { font-family: "Lexend", sans-serif; font-size: 21px; fill: var(--ink); }

  .card { position: absolute; left: 416px; width: 631px; height: 405px; overflow: hidden; }
  .card--front { top: 76px; background: var(--ink); color: var(--paper); }
  .card--back { top: 651px; background: var(--paper); border: 1px solid var(--ink); }

  .headline {
    position: absolute; left: 0; right: 0; top: 96px; text-align: center;
    font-family: "Fraunces", serif; font-weight: 900; font-size: 41px; line-height: 53px; letter-spacing: -0.5px;
  }
  .headline-mark { position: relative; display: inline-block; padding: 0 10px; color: var(--ink); }
  .headline-mark::before {
    content: ""; position: absolute; left: -8px; right: -70px; top: 6px; bottom: 2px;
    background: var(--highlight); border-radius: 4px 30px 6px 20px; transform: rotate(-2deg); z-index: 0;
  }
  .headline-mark span { position: relative; z-index: 1; }
  .back-note {
    position: absolute; left: 0; right: 0; top: 353px; text-align: center;
    font-family: "Lexend", sans-serif; font-size: 21px;
  }
  .back-note-icon { font-size: 18px; margin-right: 6px; vertical-align: 2px; }

  .back-art { position: absolute; inset: 0; }
  .hand { position: absolute; border-radius: 12px; }
  .hand--up { left: 4px; top: 22px; width: 116px; height: 108px; background: var(--hand-light); }
  .hand--down { left: 298px; top: 27px; width: 112px; height: 112px; background: var(--hand-dark); }

  .heading { position: absolute; font-family: "Fraunces", serif; font-weight: 900; line-height: 1; letter-spacing: -1px; }
  .heading--oh { left: 112px; top: 24px; font-size: 44px; }
  .heading--yes { left: 134px; top: 60px; font-size: 58px; }
  .heading--no { left: 413px; top: 22px; font-size: 58px; color: var(--paper); }
  .heading--way { left: 506px; top: 37px; font-size: 40px; color: var(--paper); font-weight: 800; }
  .heading--jose { left: 460px; top: 80px; font-size: 43px; color: var(--paper); }

  .oil-list { position: absolute; list-style: none; text-align: center; font-size: 14.5px; line-height: 24px; }
  .oil-list--ok { left: 20px; width: 252px; top: 143px; }
  .oil-list--avoid { left: 450px; width: 156px; top: 143px; color: var(--paper); }
  .cookware-notes { position: absolute; left: 0; width: 300px; top: 322px; list-style: none; text-align: center; font-size: 14.5px; line-height: 24px; }
</style>
</head>
<body>
<main class="sheet">
  <p class="side-label side-label--front">Front</p>
  <p class="side-label side-label--back">Back</p>

  <svg class="dimension" width="1200" height="520" aria-hidden="true">
    <g stroke="#0a0b0a" stroke-width="2.5" fill="none">
      <line x1="416" y1="48" x2="1047" y2="48"/>
      <line x1="416" y1="30" x2="416" y2="64"/>
      <line x1="1047" y1="30" x2="1047" y2="64"/>
      <line x1="384" y1="76" x2="384" y2="482"/>
      <line x1="367" y1="76" x2="401" y2="76"/>
      <line x1="367" y1="482" x2="401" y2="482"/>
    </g>
    <text class="dimension-text" x="721" y="23" text-anchor="middle">3.5 in</text>
    <text class="dimension-text" x="0" y="0" text-anchor="middle" transform="translate(358 279) rotate(-90)">2.25 in</text>
  </svg>

  <section class="card card--front" aria-label="Card front">
    <h1 class="headline">
      Hello, Foodie here!<br>
      with a <span class="headline-mark"><span>health-related</span></span><br>
      dietary restriction<br>
      regarding seed oils
    </h1>
    <p class="back-note"><span class="back-note-icon">✱</span>Please see back side</p>
  </section>

  <section class="card card--back" aria-label="Card back">
    <svg class="back-art" viewBox="0 0 631 405" width="631" height="405" aria-hidden="true">
      <path d="M296 0 H631 V405 H423 C420 300 300 230 272 150 C258 100 262 40 296 0 Z" fill="#0a0b0a"/>
      <path d="M314 0 C270 40 268 110 300 150 C340 200 430 260 452 405" fill="none" stroke="#ffffff" stroke-width="2"/>
      <path d="M213 0 C250 50 268 100 266 170 C266 260 300 350 396 405" fill="none" stroke="#0a0b0a" stroke-width="2"/>
    </svg>
    <div class="hand hand--up" role="img" aria-label="Line drawing of a hand giving a thumbs up"></div>
    <div class="hand hand--down" role="img" aria-label="Line drawing of a hand giving a thumbs down"></div>

    <h2 class="heading heading--oh">Oh</h2>
    <h2 class="heading heading--yes">Yes!</h2>
    <h2 class="heading heading--no">No</h2>
    <h2 class="heading heading--way">Way</h2>
    <h2 class="heading heading--jose">Jose!</h2>

    <ul class="oil-list oil-list--ok">
      <li>Butter (most preferable)</li>
      <li>Extra virgin olive oil</li>
      <li>Avocado oil</li>
      <li>Coconut oil</li>
      <li>Ghee</li>
      <li>Lard</li>
      <li>Any other animal-based fats</li>
    </ul>
    <ul class="cookware-notes">
      <li>Cross-contamination acceptable</li>
      <li>Used cookware OK, no ingredient use</li>
      <li>Separate cookware not necessary</li>
    </ul>
    <ul class="oil-list oil-list--avoid">
      <li>Vegetable oil</li>
      <li>Canola oil</li>
      <li>Soybean oil</li>
      <li>Sunflower oil</li>
      <li>Corn oil</li>
      <li>Cottonseed oil</li>
      <li>Safflower oil</li>
      <li>Peanut oil</li>
      <li>Sesame oil</li>
    </ul>
  </section>
</main>
</body>
</html>
```